We need a business card design for an Afghan catering business called 'Belvo Catering'. We provide Afghan food for any occasions such as wedding, birthday, engagement, small gathering, etc. We would like the business card to include the name of the business designed with the logo, phone number, and the address. We already have our logo that we would upload. The design that we require or suggest must be black with the logo and if possible change the colors of the logo (e.g. the logo includes red and gray lines) to gold. In other words, we would like the business card color to be black with some luxury design that would match the logo. For the front, we would like the logo which includes the name of the business, contact info, and the address. Also, depending on the design we would like to include some pictures of the food. the location (map), facebook, and instagram. After having a look at the design of the business card, we also need menu design and flyer design same thing as the business card design.

Industry/Entity Type

Business

Contact Information for Business Card

Title: Belvo Catering
Phone #: 5831046625 and 5839027148
Name: Soraya

Font styles to use
Serif
Script

Colors
000000

Requirements
Must have
• My project must have the name (with the logo), phone number, email, name, address, map, a few picture of the food, facebook, and Instagram logo.
Nice to have
• The color and font must match the logo. It must look simple and luxury (with suggested color black).

```html
<!DOCTYPE html>
<html lang="en">
<head>
<meta charset="utf-8">
<title>Belvo Catering — Business Card</title>
<link href="https://fonts.googleapis.com/css2?family=Montserrat:wght@500;600&display=swap" rel="stylesheet">
<style>
  :root {
    --black: #000000;
    --gold-deep: #8a5a1e;
    --gold-mid: #d9a22a;
    --gold-light: #f8f0b4;
    --gold-text: #d4a636;
    --page: #ffffff;
    --ink: #111111;
  }
  * { margin: 0; padding: 0; box-sizing: border-box; }
  html, body {
    width: 1200px; height: 1000px; overflow: hidden;
    background: var(--page);
    font-family: "Montserrat", Arial, sans-serif;
  }
  .canvas { position: relative; width: 1200px; height: 1000px; }

  .card { position: absolute; left: 317px; width: 567px; height: 332px; overflow: hidden; }

  /* Front */
  .card-front {
    top: 150px;
    background: linear-gradient(160deg, var(--gold-light) 0%, #f3e39a 20%, var(--gold-mid) 45%, #c9922a 60%, var(--gold-light) 82%, #b07a2a 100%);
  }
  .card-front .band {
    position: absolute; left: 0; top: 126px; width: 100%; height: 80px;
    background: var(--black);
    border-top: 2px solid var(--gold-mid);
    border-bottom: 2px solid var(--gold-mid);
  }
  .emblem {
    position: absolute; left: 175px; top: 62px; width: 208px; height: 208px;
    border-radius: 50%; background: var(--black);
    border: 3px solid var(--gold-mid);
    display: flex; flex-direction: column; align-items: center; justify-content: center;
  }
  .brand-name {
    color: var(--gold-text); font-weight: 600; text-align: center;
    line-height: 1.15; letter-spacing: 1px;
  }
  .card-front .brand-name { font-size: 26px; }

  /* Back */
  .card-back { top: 518px; background: var(--black); }
  .card-back .brand-name {
    position: absolute; left: 30px; top: 56px; width: 190px; font-size: 24px; text-align: left;
  }
  .brand-mark {
    position: absolute; left: 30px; top: 34px; width: 14px; height: 14px;
    border-radius: 50%; background: var(--gold-text);
  }
  .gold-band {
    position: absolute; left: 0; top: 181px; width: 100%; height: 123px;
    background: linear-gradient(100deg, #b37b26 0%, var(--gold-mid) 25%, var(--gold-light) 60%, #e6c260 80%, var(--gold-mid) 100%);
  }
  .contact-list {
    position: absolute; left: 30px; top: 193px; list-style: none;
    color: var(--ink); font-size: 14.5px; font-weight: 500;
  }
  .contact-list li { display: flex; align-items: center; gap: 8px; height: 18px; }
  .contact-list li.gap { margin-top: 6px; }
  .contact-list svg { width: 14px; height: 14px; flex: none; }
  .social-square { width: 12px; height: 12px; background: var(--ink); border-radius: 2px; flex: none; margin: 0 1px; }

  .food-photo {
    position: absolute; border-radius: 50%;
    border: 4px solid var(--gold-mid);
    box-shadow: 0 0 0 1px #6b4510;
  }
  .photo-carrot {
    left: 283px; top: 74px; width: 160px; height: 160px;
    background: radial-gradient(circle at 45% 50%, #e0732a 0%, #3a2a2a 45%, #d9652a 70%, #8a8a8a 100%);
  }
  .photo-fruit {
    left: 415px; top: 25px; width: 122px; height: 122px;
    background: radial-gradient(circle at 50% 50%, #e8c040 0%, #c8322a 40%, #5a8a2a 70%, #d8d0c0 100%);
  }
  .photo-platter {
    left: 399px; top: 172px; width: 124px; height: 124px;
    background: radial-gradient(circle at 50% 55%, #e0b040 0%, #a83028 45%, #6a8a30 70%, #7a6a5a 100%);
  }
</style>
</head>
<body>
<main class="canvas">

  <section class="card card-front" aria-label="Business card front">
    <div class="band"></div>
    <div class="emblem">
      <p class="brand-name">Belvo<br>Catering</p>
    </div>
  </section>

  <section class="card card-back" aria-label="Business card back">
    <span class="brand-mark"></span>
    <p class="brand-name">Belvo<br>Catering</p>

    <div class="gold-band"></div>

    <ul class="contact-list">
      <li>
        <svg viewBox="0 0 14 14"><circle cx="7" cy="7" r="7" fill="#111"/><rect x="4.5" y="2.8" width="5" height="8.4" rx="1" fill="#e8cf7a"/><rect x="5.3" y="3.8" width="3.4" height="5.4" fill="#111"/></svg>
        583 104 6625 - Soraya
      </li>
      <li>
        <svg viewBox="0 0 14 14"><circle cx="7" cy="7" r="7" fill="#111"/><rect x="4.5" y="2.8" width="5" height="8.4" rx="1" fill="#e8cf7a"/><rect x="5.3" y="3.8" width="3.4" height="5.4" fill="#111"/></svg>
        583 902 7148 - Leyla
      </li>
      <li class="gap">
        <svg viewBox="0 0 14 14"><circle cx="7" cy="7" r="7" fill="#111"/><rect x="3.5" y="4.5" width="7" height="5" fill="#e8cf7a"/><path d="M3.5 4.5 L7 7.5 L10.5 4.5" stroke="#111" stroke-width="1" fill="none"/></svg>
        belvocatering@mailbox.com
      </li>
      <li class="gap"><span class="social-square"></span>Belvo Catering - Soraya</li>
      <li><span class="social-square"></span>@belvocatering</li>
    </ul>

    <div class="food-photo photo-carrot" role="img" aria-label="Photo of an Afghan rice platter topped with carrot strips and raisins"></div>
    <div class="food-photo photo-fruit" role="img" aria-label="Photo of a colourful fresh fruit and vegetable buffet display"></div>
    <div class="food-photo photo-platter" role="img" aria-label="Photo of a catering tray with arranged fruit slices"></div>
  </section>

</main>
</body>
</html>
```